依頼詳細
・B5縦カラー(裏面1c)
・出演アーティストは2組(1.森田ユミ&ルアペドラ、2.吉川沙織&前園剛)で1.がメインアーティストです。
・写真は適宜切り抜きなどしてご使用ください。
・ルアペドラ全員写真+青木カナ1人(写真1,2 いずれか)+ロゴ(適宜着色など)+吉川沙織&前園剛をレイアウトお願いします。

納品時にはSNSなどに使用するバナー画像作成もあわせてお願いいたします。
・コンペでは表面デザインとバナー(横 16:9 )のみお願いします。
決定後裏面に記載する詳細情報をお知らせして仕上げていただきたいと思います。
・バナー画像には詳細テキスト情報は原則として不要です
記載項目
【タイトル】凍てつく宵のフェスタ
【日付】2022年12月16日(金)
【会場名】代官山 ゆうべの窓に灯ともして
渋谷区代官山町14-7
ルミエール代官山B1
【出演者名】
・森田ユミ&ルア・ペドラ
(森田ユミ vocal、杉本健二 sax、大塚理恵 cl、沢井隆史 sax、今野英樹 sax、柳田さえ perc、西川昭夫 bass、川端修平 drums、野口康弘 guitar)
・吉川沙織 vocal & 前園剛 8st-guitar

【時間、料金】
開場 18:30
開演 19:30
前売4000円
当日4500円
(共に+1ドリンク代600円)
サイズ
B5
ページ数
両面
希望イメージ
シンプル 複雑
単色 カラフル
暗い 明るい
日常 高級
遊び心 厳粛
未来的 伝統的
女性的 男性的
希望する色
ライブタイトル、内容にふさわしい色をご提案いただければ幸いです。
納品ファイル
• 高解像度JPG (.jpg)
• イラストレーター形式 (.ai)
• PNG形式 (.png)
補足説明
ルア・ペドラ
ブラジル在住歴22年の森田ユミが日本に帰国後、ブラジルで培ってきた4本サックスがあるラテンコンボを日本で再結成したいと思い出来たのがこのルア・ペドラです。森田ユミのオリジナル曲を中心に、ラテンチックなサウンドにとことん楽しさを追求するコンセプトです。特にライブの後半にはブラジル北東部のカーニバル体験が出来て、思わず心と体が踊り出すことでしょう。

季節感とイベント内容に即したデザインでアーティストにも気に入ってもらえました。

この度は多くのご提案をいただきありがとうございました。
いいデザインが沢山あり絞るのが大変でした。
当選とできなかった皆様にはまた別の機会にお願い出来ればと思っております。
ありがとうございました。

```html
<!DOCTYPE html>
<html lang="ja">
<head>
<meta charset="utf-8">
<title>凍てつく宵のフェスタ</title>
<link rel="stylesheet" href="https://fonts.googleapis.com/css2?family=M+PLUS+Rounded+1c:wght@500;800;900&family=Noto+Sans+JP:wght@400;500;700;900&display=swap">
<style>
:root{
  --cream:#fcecb0;
  --cream-deep:#f6dc8a;
  --sun:#f5c945;
  --orange:#e9692a;
  --red:#d8402f;
  --navy:#1f3566;
  --ink:#2b2b2b;
  --white:#ffffff;
  --green:#4f9a57;
  --photo-warm:#b88a5e;
  --photo-dark:#5a4636;
}
*{margin:0;padding:0;box-sizing:border-box}
html,body{width:848px;height:1200px;overflow:hidden;background:var(--cream)}
body{font-family:"Noto Sans JP",sans-serif;color:var(--ink)}
.flyer{position:relative;width:848px;height:1200px;background:linear-gradient(var(--cream) 0 720px,var(--cream-deep) 720px);overflow:hidden}
.art{position:absolute}
.art-festoon{left:0;top:0;width:848px;height:250px;background:linear-gradient(100deg,#e7553a 0%,#f2b33d 30%,#63a95c 55%,#f08a3c 78%,#3f7fbf 100%);opacity:.55;border-radius:0 0 40px 40px}
.art-left{left:20px;top:250px;width:110px;height:200px;border-radius:50px;background:linear-gradient(#f2a04a,#5aa05e);opacity:.55}
.art-right{right:20px;top:250px;width:110px;height:200px;border-radius:50px;background:linear-gradient(#e9563a,#f5c945);opacity:.55}
.art-fire{left:330px;top:560px;width:190px;height:150px;border-radius:90px 90px 30px 30px;background:radial-gradient(circle at 50% 70%,#ffd34a,#f07a2c 55%,#c8492c);opacity:.85}
.title{position:absolute;left:0;top:262px;width:848px;text-align:center;font-family:"M PLUS Rounded 1c",sans-serif;font-weight:900;color:var(--orange);-webkit-text-stroke:8px var(--white);paint-order:stroke fill;line-height:1.02;letter-spacing:4px}
.title .l1{display:block;font-size:108px}
.title .l2{display:block;font-size:118px}
.date{position:absolute;left:0;top:498px;width:848px;text-align:center;font-family:"M PLUS Rounded 1c",sans-serif;font-weight:800;font-size:42px;color:var(--navy)}
.date .dow{display:inline-block;width:52px;height:52px;border-radius:50%;background:var(--navy);color:var(--white);font-size:30px;line-height:52px;margin-left:8px;vertical-align:4px}
.tag{display:block;text-align:center;font-size:14px;font-weight:700;color:var(--navy);letter-spacing:4px;margin-bottom:6px}
.cast{position:absolute;left:40px;top:575px;width:290px;text-align:center}
.cast .main{font-size:22px;font-weight:900;color:var(--navy)}
.cast .sub{font-size:16px;font-weight:700;color:var(--navy);margin-top:6px}
.venue{position:absolute;right:40px;top:575px;width:270px;text-align:center;color:var(--navy)}
.venue .name{font-size:19px;font-weight:900;line-height:1.3}
.venue .addr{font-size:13px;margin-top:6px;line-height:1.5}
.wordmark{position:absolute;left:28px;top:760px;display:flex;align-items:center;gap:12px;font-family:"M PLUS Rounded 1c",sans-serif;font-weight:900;font-size:34px;color:var(--navy);line-height:1.05}
.wordmark .dot{width:34px;height:34px;border-radius:50%;background:var(--sun)}
.photo{position:absolute;border-radius:6px}
.photo-band{left:355px;top:748px;width:300px;height:180px;background:linear-gradient(135deg,var(--photo-warm),var(--photo-dark))}
.photo-singer{left:28px;top:850px;width:310px;height:320px;background:linear-gradient(160deg,#3c3a40,#8a6b55);border-radius:0 0 6px 6px}
.photo-duo{left:560px;top:1015px;width:260px;height:140px;background:linear-gradient(135deg,#c9a57c,#6e5a48)}
.band-label{position:absolute;left:355px;top:938px;width:210px;background:var(--sun);color:var(--navy);font-size:15px;font-weight:900;text-align:center;padding:5px 0;border-radius:3px}
.members{position:absolute;left:360px;top:975px;width:195px;font-size:12px;line-height:1.65;color:var(--ink);list-style:none}
.info{position:absolute;left:680px;top:760px;width:150px;text-align:center;color:var(--navy)}
.info .row{font-size:17px;font-weight:700;line-height:1.5}
.info .note{font-size:11px;line-height:1.5;margin-top:2px}
.info .block+.block{margin-top:22px}
.duo-caption{position:absolute;left:560px;top:1162px;width:260px;text-align:center;font-size:13px;font-weight:700;color:var(--navy)}
.singer-caption{position:absolute;left:28px;top:1140px;width:310px;text-align:center;font-size:18px;font-weight:900;color:var(--white)}
</style>
</head>
<body>
<main class="flyer">
  <div class="art art-festoon" role="img" aria-label="旗飾り、風船、マラカス、ホットドッグ、ランタンのカーニバル風イラスト"></div>
  <div class="art art-left" role="img" aria-label="サボテンとマラカスのイラスト"></div>
  <div class="art art-right" role="img" aria-label="ギターとランタンのイラスト"></div>

  <h1 class="title"><span class="l1">凍てつく宵の</span><span class="l2">フェスタ</span></h1>
  <p class="date">2022年12月16日<span class="dow">金</span></p>

  <section class="cast">
    <span class="tag">― 出 演 ―</span>
    <p class="main">森田ユミ&amp;<br>ルア・ペドラ</p>
    <p class="sub">吉川沙織 vocal &amp;<br>前園剛 8st-guitar</p>
  </section>

  <div class="art art-fire" role="img" aria-label="焚き火のイラスト"></div>

  <section class="venue">
    <span class="tag">― 会 場 ―</span>
    <p class="name">代官山<br>ゆうべの窓に灯ともして</p>
    <p class="addr">渋谷区代官山町14-7<br>ルミエール代官山B1</p>
  </section>

  <div class="wordmark"><span class="dot"></span><span>Yumi &amp;<br>Lua Pedra</span></div>

  <div class="photo photo-band" role="img" aria-label="ルア・ペドラのメンバー集合写真"></div>
  <div class="photo photo-singer" role="img" aria-label="ボーカル森田ユミのポートレート写真"></div>
  <p class="singer-caption">森田ユミ&amp;ルア・ペドラ</p>

  <p class="band-label">森田ユミ&amp;ルア・ペドラ</p>
  <ul class="members">
    <li>森田ユミ vocal</li>
    <li>杉本健二 sax ／ 大塚理恵 cl</li>
    <li>沢井隆史 sax ／ 今野英樹 sax</li>
    <li>柳田さえ perc ／ 西川昭夫 bass</li>
    <li>川端修平 drums</li>
    <li>野口康弘 guitar</li>
  </ul>

  <section class="info">
    <div class="block">
      <span class="tag">― 時 間 ―</span>
      <p class="row">開場 18:30</p>
      <p class="row">開演 19:30</p>
    </div>
    <div class="block">
      <span class="tag">― 料 金 ―</span>
      <p class="row">前売 4000円</p>
      <p class="row">当日 4500円</p>
      <p class="note">共に+1ドリンク代<br>600円</p>
    </div>
  </section>

  <div class="photo photo-duo" role="img" aria-label="吉川沙織と前園剛のデュオ写真"></div>
  <p class="duo-caption">吉川沙織 vocal &amp; 前園剛 8st-guitar</p>
</main>
</body>
</html>
```